Layout of a white paper from an already written word document

We are a consulting company specializing in General Data Protection Regulation (GDPR) and cybersecurity. We wish to publish a white paper on our methodologies. The text is ready and we would like it to be laid out in a neat design.
Our target is SMEs and mid-caps.
We try to provide very concrete and pragmatic solutions to our clients. Attached is a sample white paper that we appreciate and the text to format.
Our web site: www.marlow-vantage.net
Target Market(s)
SMEs and mid-caps
Requirements
Must have
- A4 Format

```html
<!DOCTYPE html>
<html lang="fr">
<head>
<meta charset="utf-8">
<title>RGPD et Cyberattaques – Livre blanc</title>
<link href="https://fonts.googleapis.com/css2?family=Montserrat:wght@700;800&display=swap" rel="stylesheet">
<style>
  :root {
    --page-bg: #e6e7e9;
    --paper: #ffffff;
    --sky: #0bb8e2;
    --mist: #eeeeee;
    --lime: #bad24b;
    --ink: #2d2626;
  }
  * { box-sizing: border-box; margin: 0; padding: 0; }
  html, body {
    width: 1030px;
    height: 1200px;
    overflow: hidden;
    background: var(--page-bg);
  }
  .cover {
    position: absolute;
    left: 66px;
    top: 20px;
    width: 897px;
    height: 1160px;
    background: var(--paper);
    overflow: hidden;
    box-shadow: 0 2px 10px rgba(0,0,0,0.12);
  }
  .cover-bands {
    position: absolute;
    inset: 0;
    width: 100%;
    height: 100%;
  }
  .brand {
    position: absolute;
    left: 633px;
    top: 78px;
    width: 220px;
    display: flex;
    flex-direction: column;
    align-items: center;
    gap: 16px;
  }
  .brand-dot {
    width: 74px;
    height: 74px;
    border-radius: 50%;
    background: var(--sky);
  }
  .brand-name {
    font-family: "Montserrat", sans-serif;
    font-weight: 700;
    font-size: 25px;
    line-height: 1.15;
    letter-spacing: 1px;
    color: var(--sky);
    text-align: center;
  }
  .title {
    position: absolute;
    left: 282px;
    top: 434px;
    font-family: "Montserrat", sans-serif;
    font-weight: 800;
    font-size: 45px;
    line-height: 61px;
    color: var(--ink);
    white-space: nowrap;
  }
</style>
</head>
<body>
  <main class="cover">
    <svg class="cover-bands" viewBox="0 0 897 1160" preserveAspectRatio="none" aria-hidden="true">
      <defs>
        <linearGradient id="sky-fade" x1="0" y1="0" x2="0" y2="1">
          <stop offset="0.05" stop-color="#ffffff"/>
          <stop offset="0.45" stop-color="#9fe0f2"/>
          <stop offset="0.85" stop-color="#0bb8e2"/>
        </linearGradient>
      </defs>
      <polygon class="band-sky" fill="url(#sky-fade)" points="0,0 120,0 230,1160 0,1160"/>
      <polygon class="band-mist" fill="var(--mist)" points="897,640 897,760 420,1160 280,1160"/>
      <polygon class="band-lime" fill="var(--lime)" points="897,760 897,1160 420,1160"/>
    </svg>

    <div class="brand">
      <span class="brand-dot"></span>
      <p class="brand-name">MARLOW<br>VANTAGE</p>
    </div>

    <h1 class="title">RGPD et Cyberattaques<br>4 actions pour assurer<br>et rassurer</h1>
  </main>
</body>
</html>
```